New Business Card for Casual Beachfront Cafe

Quirky Beachfront Cafe at Moana, South Australia needs a DOUBLE SIDED business card to print on PrintHarbor.

Target Market(s)

Business Cards sit on the counter for Guests to take with them. Please view our website www.saltreefcafe.com.au to get a feel for the Cafe. You may also view our Instagram at @saltreefcafe

Industry/Entity Type

Cafe / Restaurant

Contact Information for Business Card

Information equivalent to: Breakfast, Lunch, Dinner, Coffee, Takeaway / 117 Parade Moana SA 5169 / Menu & Opening Hours: www.saltreefcafe.com.au / ph (08) 8461 9273

Requirements
Must have
• Information equivalent to: Breakfast, Lunch, Dinner, Coffee, Takeaway / 117 Parade Moana SA 5169 / Menu & Opening Hours: www.saltreefcafe.com.au / ph (08) 8461 9273
Nice to have
• Potentially some of our trademark colours (Cafe can be searched via Seekly)
Should not have
• Must NOT have image of the building. May have the logo provided on one side but not necessarily, depending on how you wish to design the card

```html
<!DOCTYPE html>
<html lang="en">
<head>
<meta charset="utf-8">
<title>Salt Reef Cafe – Business Card Presentation</title>
<link rel="stylesheet" href="https://fonts.googleapis.com/css2?family=Ubuntu:wght@400;500;700&display=swap">
<style>
  :root {
    --yellow: #ffff00;
    --rust: #b45519;
    --navy: #15467c;
    --white: #ffffff;
    --shadow: rgba(0, 0, 0, 0.55);
  }
  * { margin: 0; padding: 0; box-sizing: border-box; }
  html, body { width: 1200px; height: 1200px; overflow: hidden; background: var(--white); }
  body { position: relative; font-family: "Ubuntu", sans-serif; }

  .corner-accent { position: absolute; left: 0; top: 0; }

  .card {
    position: absolute;
    width: 653px;
    height: 372px;
    background: var(--rust);
    box-shadow: 22px 18px 14px -4px var(--shadow);
  }
  .card--front { left: 52px; top: 192px; }
  .card--back { left: 51px; top: 594px; }
  .card__face {
    position: absolute;
    left: 15.5px; top: 15.5px; right: 15.5px; bottom: 15.5px;
    background: var(--yellow);
  }
  .card__tab {
    position: absolute;
    left: 59px; width: 536px;
    bottom: -15.5px; height: 54px;
    background: var(--rust);
    border-radius: 20px 20px 0 0;
    color: var(--yellow);
    display: flex; align-items: center; justify-content: center;
  }
  .card__tab--services { font-size: 25px; font-weight: 400; letter-spacing: 0.2px; padding-bottom: 12px; }
  .card__tab--url { font-size: 27px; font-weight: 400; letter-spacing: 4.6px; padding-bottom: 12px; }

  .splash {
    position: absolute;
    left: 0; top: 7px;
    width: 78px; height: 114px;
    background: var(--rust);
    border-radius: 0 40px 40px 0;
  }

  .contact { position: absolute; left: 28px; color: var(--navy); font-size: 16.5px; line-height: 20px; }
  .contact__icon { position: absolute; left: 0; }
  .contact__text { position: absolute; left: 27px; top: 0; white-space: nowrap; }
  .contact__label { font-weight: 500; }
  .contact--phone { top: 142px; }
  .contact--web { top: 181px; }
  .contact--address { top: 233px; }

  .building-art { position: absolute; background: linear-gradient(180deg, rgba(21,70,124,0.12), rgba(21,70,124,0.22)); }
  .building-art--on-navy { background: linear-gradient(180deg, rgba(255,255,255,0.14), rgba(255,255,255,0.24)); }

  .brand-name {
    position: absolute;
    text-align: center;
    font-family: "Ubuntu", sans-serif;
    font-weight: 700;
    color: var(--navy);
    line-height: 1;
    text-transform: uppercase;
  }
  .brand-name__line { display: block; }
  .brand-name--white { color: var(--white); }

  .panel { position: absolute; left: 752px; width: 448px; }
  .panel--yellow { top: 53px; height: 530px; background: var(--yellow); border-top-left-radius: 100px; }
  .panel--navy { top: 583px; height: 585px; background: var(--navy); border-bottom-left-radius: 95px; }
</style>
</head>
<body>

  <svg class="corner-accent" width="127" height="127" viewBox="0 0 127 127" aria-hidden="true">
    <polygon points="0,0 127,0 0,127" fill="var(--rust)"/>
  </svg>

  <section class="card card--front" aria-label="Business card front">
    <div class="card__face">
      <div class="splash" role="img" aria-label="Decorative rust-coloured splash in the corner"></div>

      <div class="contact contact--phone">
        <svg class="contact__icon" width="16" height="25" viewBox="0 0 18 26" aria-hidden="true" style="top:-2px;">
          <rect x="1.5" y="1.5" width="15" height="23" rx="2.5" fill="none" stroke="var(--navy)" stroke-width="2.6"/>
          <rect x="3.5" y="4" width="11" height="15" fill="var(--navy)"/>
          <circle cx="9" cy="21.8" r="1.1" fill="var(--yellow)"/>
        </svg>
        <span class="contact__text">(08) 8461 9273</span>
      </div>

      <div class="contact contact--web">
        <svg class="contact__icon" width="22" height="22" viewBox="0 0 24 24" aria-hidden="true" style="top:10px;left:-4px;">
          <g fill="none" stroke="var(--navy)" stroke-width="1.6">
            <circle cx="12" cy="12" r="10.5"/>
            <ellipse cx="12" cy="12" rx="4.8" ry="10.5"/>
            <line x1="1.5" y1="12" x2="22.5" y2="12"/>
            <path d="M3.5 6.5 H20.5 M3.5 17.5 H20.5"/>
          </g>
        </svg>
        <span class="contact__text"><span class="contact__label">Menu &amp; Opening Hours</span><br>www.saltreefcafe.com.au</span>
      </div>

      <div class="contact contact--address">
        <svg class="contact__icon" width="16" height="22" viewBox="0 0 18 24" aria-hidden="true" style="top:20px;left:-1px;">
          <path d="M9 0 C4 0 0 4 0 9 C0 15 9 24 9 24 C9 24 18 15 18 9 C18 4 14 0 9 0 Z" fill="var(--navy)"/>
          <circle cx="9" cy="9" r="3.4" fill="var(--yellow)"/>
        </svg>
        <span class="contact__text"><span class="contact__label">Takeaway</span><br>117 Parade Moana SA<br>5169</span>
      </div>

      <div class="building-art" role="img" aria-label="Line sketch of the beachfront cafe storefront" style="left:265px; top:41px; width:323px; height:125px;"></div>

      <div class="brand-name" style="left:280px; top:172px; width:275px;">
        <span class="brand-name__line" style="font-size:44px;">Salt Reef</span>
        <span class="brand-name__line" style="font-size:60px; margin-top:6px;">Cafe</span>
      </div>

      <div class="card__tab card__tab--services">BREAKFAST , LUNCH, DINNER, COFFEE</div>
    </div>
  </section>

  <section class="card card--back" aria-label="Business card back">
    <div class="card__face">
      <div class="building-art" role="img" aria-label="Line sketch of the beachfront cafe storefront" style="left:132px; top:24px; width:360px; height:140px;"></div>

      <div class="brand-name" style="left:158px; top:178px; width:300px;">
        <span class="brand-name__line" style="font-size:46px;">Salt Reef</span>
        <span class="brand-name__line" style="font-size:62px; margin-top:6px;">Cafe</span>
      </div>

      <div class="card__tab card__tab--url">www.saltreefcafe.com.au</div>
    </div>
  </section>

  <section class="panel panel--yellow" aria-label="Logo on yellow">
    <div class="building-art" role="img" aria-label="Line sketch of the beachfront cafe storefront" style="left:32px; top:146px; width:396px; height:152px;"></div>
    <div class="brand-name" style="left:60px; top:312px; width:330px;">
      <span class="brand-name__line" style="font-size:52px;">Salt Reef</span>
      <span class="brand-name__line" style="font-size:70px; margin-top:6px;">Cafe</span>
    </div>
  </section>

  <section class="panel panel--navy" aria-label="Logo on navy">
    <div class="building-art building-art--on-navy" role="img" aria-label="Line sketch of the beachfront cafe storefront" style="left:40px; top:147px; width:397px; height:152px;"></div>
    <div class="brand-name brand-name--white" style="left:70px; top:314px; width:330px;">
      <span class="brand-name__line" style="font-size:52px;">Salt Reef</span>
      <span class="brand-name__line" style="font-size:70px; margin-top:6px;">Cafe</span>
    </div>
  </section>

</body>
</html>
```